| 希望する色 | オレンジ系 追記事項: 希望としていますが、サイトをご確認頂き、合う色味があればそちらで作成頂き問題ありません。 |
| 弊社で運営しております、ソラテックというサービスに掲載する、購買意欲向上の為、 訴求バナーを掲載したいと考えております。 また、ABテストや、ケース別で掲載を変更したく、今回は3件の募集をさせて頂きます。 サイト自体は青系の色を基調とし構築されております。 https://soratecku-web.jp/shop-item.html 【訴求文言】 導線ではなく、購入を促進させる目的である為、以下の文言を挿入、強調をお願いします。 --------------------------- ・90日間保証 ・全国送料無料 ・メーカー純正キー ・年間1万本の作成実績 ・簡単1分注文 ---------------------------- |
キーワードの使用方法、デザインのバランスもとてもよく、
かつ、わかりやすい印象がありましたので、1案目として採用をさせて頂きます。
皆様からの沢山のご提案、ありがとうございました。
どの案も素晴らしく、弊社内でも採用に関して意見が分かれる程でした。
また、機会がありましたら皆様からご応募頂けますと幸いです。

```html
<!DOCTYPE html>
<html lang="ja">
<head>
<meta charset="utf-8">
<title>ソラテック 簡単1分注文バナー</title>
<link rel="stylesheet" href="https://fonts.googleapis.com/css2?family=M+PLUS+Rounded+1c:wght@500;800;900&display=swap">
<style>
  :root {
    --sky: #1e8fd8;
    --sky-deep: #1565b8;
    --sky-pale: #cfe6f7;
    --sky-soft: #e6f2fb;
    --ink: #111111;
    --white: #ffffff;
    --metal: #c9ced3;
    --metal-light: #eef0f2;
    --alert: #e02020;
    --logo: #3aa6d8;
  }
  * { margin: 0; padding: 0; box-sizing: border-box; }
  html, body { width: 1200px; height: 324px; overflow: hidden; background: var(--white); }
  .banner {
    position: relative;
    width: 1200px;
    height: 324px;
    overflow: hidden;
    font-family: "M PLUS Rounded 1c", sans-serif;
    background: var(--white);
  }
  .banner__backdrop {
    position: absolute;
    left: 0; top: 0;
    width: 1200px; height: 324px;
    background: linear-gradient(180deg, var(--white) 0%, var(--white) 28%, var(--sky-soft) 45%, var(--sky-pale) 100%);
  }
  .brand {
    position: absolute;
    left: 14px; top: 14px;
    font-weight: 800;
    font-size: 30px;
    color: var(--logo);
    letter-spacing: 1px;
  }
  .key-photo {
    position: absolute;
    border-radius: 40px;
    background: linear-gradient(160deg, var(--metal-light) 0%, var(--metal) 60%, #a9b0b7 100%);
  }
  .key-photo--left { left: 40px; top: 48px; width: 170px; height: 266px; }
  .key-photo--right { left: 975px; top: 10px; width: 215px; height: 300px; }
  .bubbles { position: absolute; left: 0; top: 0; width: 1200px; height: 120px; }
  .bubble-label {
    position: absolute;
    font-weight: 800;
    font-size: 25px;
    color: var(--ink);
    white-space: nowrap;
    transform: translate(-50%, -50%);
  }
  .headline {
    position: absolute;
    left: 0; top: 150px;
    width: 1200px;
    text-align: center;
    font-weight: 900;
    font-size: 104px;
    line-height: 1;
    color: var(--sky);
    letter-spacing: 14px;
    -webkit-text-stroke: 3px var(--white);
    paint-order: stroke fill;
    text-shadow: 4px 5px 0 var(--sky-deep), 0 0 10px rgba(255,255,255,0.9);
  }
  .shipping-badge {
    position: absolute;
    left: 1005px; top: 250px;
    width: 170px; height: 60px;
    background: var(--sky-deep);
    border-radius: 8px;
    display: flex;
    align-items: center;
    justify-content: center;
    gap: 3px;
    padding: 0 8px;
  }
  .shipping-badge span {
    display: block;
    background: var(--white);
    color: var(--alert);
    font-weight: 900;
    font-size: 21px;
    width: 25px;
    text-align: center;
    line-height: 28px;
  }
</style>
</head>
<body>
<div class="banner">
  <div class="banner__backdrop" role="img" aria-label="白から水色へ続く格子柄の背景"></div>

  <div class="brand">ソラテック</div>

  <div class="key-photo key-photo--left" role="img" aria-label="銀色の純正合鍵2本の写真"></div>
  <div class="key-photo key-photo--right" role="img" aria-label="銀色の純正合鍵2本の写真"></div>

  <svg class="bubbles" viewBox="0 0 1200 120" aria-hidden="true">
    <g fill="#ffffff" stroke="#111111" stroke-width="3">
      <ellipse cx="368" cy="62" rx="112" ry="44"/>
      <ellipse cx="566" cy="60" rx="82" ry="42"/>
      <ellipse cx="808" cy="58" rx="138" ry="46"/>
    </g>
  </svg>
  <div class="bubble-label" style="left:368px;top:62px;">メーカー純正キー</div>
  <div class="bubble-label" style="left:566px;top:60px;">90日間保証</div>
  <div class="bubble-label" style="left:808px;top:58px;">年間1万本の作成実績</div>

  <h1 class="headline">簡単 1 分注文</h1>

  <div class="shipping-badge" aria-label="全国送料無料">
    <span>全</span><span>国</span><span>送</span><span>料</span><span>無</span><span>料</span>
  </div>
</div>
</body>
</html>
```